High Quality Flyer Design For Real Estate Website

I require a double sided flyer for the website tallowbrookhomes.net.

The flyer size should be A5.

The flyer must be fresh and up to date and go with the theme of the website.
Updates

Old flyer attachment was missing, but is now attached.

Target Market(s)

Landlords and people looking to buy or sell their house of all age groups

Industry/Entity Type

Real Estate

Font styles to use
Sans Serif

Requirements
Must have
• The main colour of the flyer should be the yellow used on the website.

The logo from the website should also be used (attached)

The text included on the old flyer must be on the new flyer (see attachment)

The flyer should take the reader through a process (see old attached flyer) and make them feel that using the website is very simple.

Nice to have

```html
<!DOCTYPE html>
<html lang="en">
<head>
<meta charset="utf-8">
<title>Tallowbrookhomes Flyer</title>
<link href="https://fonts.googleapis.com/css2?family=Arimo:wght@400;700&display=swap" rel="stylesheet">
<style>
  :root {
    --backdrop: #d3893b;
    --card-yellow: #e7d62b;
    --bar-yellow: #f7c600;
    --badge-yellow: #f9c800;
    --ink: #111111;
    --black: #000000;
    --url-yellow: #f2d42a;
  }
  * { margin: 0; padding: 0; box-sizing: border-box; }
  html, body {
    width: 1200px; height: 916px; overflow: hidden;
    background: var(--backdrop);
    font-family: "Arimo", Arial, sans-serif;
    color: var(--ink);
  }
  .canvas { position: relative; width: 1200px; height: 916px; }
  .flyer {
    position: absolute; left: 120px; top: 54px; width: 959px; height: 816px;
    background: var(--card-yellow);
    box-shadow: 6px 6px 6px rgba(0,0,0,0.55);
  }
  .abs { position: absolute; }
  .brand-box {
    left: 95px; top: 65px; width: 309px; height: 85px;
    background: var(--black);
    display: flex; align-items: center; justify-content: center; gap: 10px;
  }
  .brand-box .mark { width: 14px; height: 14px; background: var(--bar-yellow); }
  .brand-box .brand-name { color: var(--bar-yellow); font-size: 24px; font-weight: 400; }
  .promise {
    left: 93px; width: 311px; height: 41px;
    background: var(--bar-yellow);
    font-size: 14px; letter-spacing: 0.2px;
    display: flex; align-items: center; padding-left: 25px;
  }
  .promise.sell { top: 195px; }
  .promise.free { top: 251px; }
  .promise.fees { top: 308px; }
  .hero-photo {
    left: 632px; top: 70px; width: 250px; height: 250px; border-radius: 50%;
    border: 3px solid var(--black);
    background: radial-gradient(circle at 50% 55%, #f4f1c8 0%, #9fb86a 30%, #3c4a3a 60%, #1f2526 100%);
  }
  .site-title {
    right: 80px; top: 326px;
    font-size: 40px; font-weight: 700; color: #222;
    text-shadow: 2px 2px 2px rgba(0,0,0,0.45);
  }
  .url-band {
    left: 93px; top: 392px; width: 787px; height: 61px; background: var(--black);
    display: flex; align-items: center; justify-content: center;
    color: var(--url-yellow); font-size: 26px;
    text-shadow: 1px 1px 1px rgba(0,0,0,0.8);
  }
  .step-tag {
    left: 93px; width: 110px; height: 48px; background: var(--black);
    display: flex; align-items: center; padding-left: 22px; gap: 10px;
    color: var(--badge-yellow); font-size: 21px;
  }
  .step-tag .num {
    width: 30px; height: 30px; border-radius: 50%; background: var(--badge-yellow);
    color: var(--ink); font-size: 19px;
    display: flex; align-items: center; justify-content: center;
  }
  .step-1 { top: 487px; }
  .step-2 { top: 579px; }
  .step-3 { top: 670px; }
  .step-text { left: 115px; font-size: 20px; }
  .text-1 { top: 548px; }
  .text-2 { top: 636px; }
  .text-3 { top: 737px; }
  .pitch { left: 485px; font-size: 20px; line-height: 25.5px; white-space: nowrap; }
  .pitch-1 { top: 474px; }
  .pitch-2 { top: 601px; }
  .wide { word-spacing: 2px; }
</style>
</head>
<body>
<div class="canvas">
  <div class="flyer">
    <div class="abs brand-box"><span class="mark"></span><span class="brand-name">tallowbrookhomes.net</span></div>

    <div class="abs promise sell">SELL OR RENT YOUR PROPERTY.</div>
    <div class="abs promise free">COMMISSION FREE.</div>
    <div class="abs promise fees">&amp; SAY GOODBYE TO AGENT FEES</div>

    <div class="abs hero-photo" role="img" aria-label="Photo of one hand passing a small model house to another open hand above green grass"></div>
    <div class="abs site-title">Tallowbrookhomes</div>

    <div class="abs url-band">www.tallowbrookhomes.net</div>

    <div class="abs step-tag step-1">Step <span class="num">1</span></div>
    <div class="abs step-text text-1">Go to tallowbrookhomes.net</div>
    <div class="abs step-tag step-2">Step <span class="num">2</span></div>
    <div class="abs step-text text-2">Create an account</div>
    <div class="abs step-tag step-3">Step <span class="num">3</span></div>
    <div class="abs step-text text-3">Upload your property using simple step by step process</div>

    <p class="abs pitch pitch-1">Once your property is uploaded,any<br>interested buyers and&nbsp;&nbsp; tenants can<br><span class="wide">contact you directly,to negotiate a price</span><br>saving you $1000’s in Estate Agent Fees</p>
    <p class="abs pitch pitch-2">For a limited time only,we are offering you<br>the opportunity to use our new website for<br>free to Buy,Sell or Let Your next property.</p>
  </div>
</div>
</body>
</html>
```